Modern & Fresh Sumeray Book Cover

Need a creative e-book cover for my book.

Title: Get Sumeray Sorted
Subtitle: Learn How To Easily Choose & Enroll in the Perfect Coverage at the Perfect Time.

Target Market(s)

60-70 year olds in the United States

Font styles to use
Sans Serif

Colors
9bcb3c
33a6d7

Requirements
Must have
• Must look modern and fresh.
• Use our company colors www.BrovaMint.com

```html
<!DOCTYPE html>
<html lang="en">
<head>
<meta charset="utf-8">
<title>Get Sumeray Sorted – Book Cover</title>
<link rel="stylesheet" href="https://fonts.googleapis.com/css2?family=Archivo+Black&family=Archivo:wght@800&family=Oswald:wght@600&display=swap">
<style>
  :root {
    --brand-blue: #33a6d7;
    --brand-green: #9bcb3c;
    --rule-green: #8cc63f;
    --ink: #111111;
    --paper: #ffffff;
    --backdrop: #e9e9e7;
    --art-light: #4fa56e;
    --art-dark: #2a7a5c;
  }
  * { box-sizing: border-box; margin: 0; padding: 0; }
  html, body {
    width: 1200px;
    height: 800px;
    overflow: hidden;
    background: var(--backdrop);
  }
  .stage {
    width: 1200px;
    height: 800px;
    display: flex;
    align-items: center;
    justify-content: center;
  }
  .cover {
    position: relative;
    width: 480px;
    height: 760px;
    background: var(--paper);
    overflow: hidden;
    box-shadow: 0 10px 30px rgba(0,0,0,0.12);
  }
  .cover-title {
    position: absolute;
    top: 44px;
    left: 0;
    right: 0;
    text-align: center;
    font-family: "Archivo Black", "Arial Black", sans-serif;
    font-weight: 400;
    color: var(--brand-blue);
    line-height: 0.92;
    text-transform: uppercase;
  }
  .cover-title span { display: block; }
  .title-small { font-size: 76px; }
  .title-large { font-size: 78px; letter-spacing: -1px; }
  .cover-subtitle {
    position: absolute;
    top: 296px;
    left: 28px;
    right: 28px;
    padding: 9px 0 8px;
    border-top: 2px solid var(--rule-green);
    border-bottom: 2px solid var(--rule-green);
    text-align: center;
    font-family: "Archivo", "Arial", sans-serif;
    font-weight: 800;
    font-size: 13.5px;
    line-height: 1.3;
    color: var(--ink);
    text-transform: uppercase;
  }
  .cover-illustration {
    position: absolute;
    top: 372px;
    left: 40px;
    width: 400px;
    height: 290px;
    border-radius: 6px;
    background: linear-gradient(180deg, var(--art-light) 0%, var(--art-dark) 100%);
    z-index: 1;
  }
  .author-band {
    position: absolute;
    left: 0;
    right: 0;
    bottom: 0;
    height: 132px;
    background: var(--brand-green);
    display: flex;
    align-items: flex-end;
    justify-content: center;
    padding-bottom: 28px;
  }
  .author-name {
    font-family: "Oswald", "Arial Narrow", sans-serif;
    font-weight: 600;
    font-size: 36px;
    color: var(--ink);
    letter-spacing: 0.5px;
    text-transform: uppercase;
  }
</style>
</head>
<body>
  <main class="stage">
    <article class="cover">
      <h1 class="cover-title">
        <span class="title-small">Get</span>
        <span class="title-large">Sumeray</span>
        <span class="title-small">Sorted</span>
      </h1>
      <p class="cover-subtitle">Learn how to easily choose &amp; enroll<br>in the perfect coverage at the perfect time</p>
      <div class="author-band">
        <p class="author-name">Author’s Name</p>
      </div>
      <div class="cover-illustration" role="img" aria-label="Illustration of a smiling older couple embracing in front of green leafy plants with small birds flying above"></div>
    </article>
  </main>
</body>
</html>
```